Harborline Energy - needs a business card

Harborline Energy is a U.S. based diesel sourcing and distribution company that supports American oil & gas fields through providing quality product and consistent services.

Target Market(s)

Oil and Gas

Contact Information for Business Card

The background of the card must be white to ensure the logo pops.

Font styles to use
Serif
Sans Serif

Colors

Designer to choose colors to be used in the design.

Requirements
Must have
• Front of Card: Tag line: Harborline Energy, Powering America's Oil & Gas fields.
• Not sure if you guys do this part but just in case...
• Dale Menschow
• Owner/CEO
• C:555.318.4076
• E:Dmenschow@harborlineenergy.example
• W:Harborlineenergy.example
• Locations: Servicing the Powder River, DJ basin and Bakken formations.
• Back of Card: " Frac fueling is what we do. We understand how important diesel fuel is to your operation, which is why our main service line is Frac fueling. We assure our supply and stand by our service"

```html
<!DOCTYPE html>
<html lang="en">
<head>
<meta charset="utf-8">
<title>Harborline Energy – Business Card</title>
<link href="https://fonts.googleapis.com/css2?family=Jost:wght@400;500;700&display=swap" rel="stylesheet">
<style>
  :root {
    --navy: #0c2b5c;
    --red: #c3202e;
    --paper: #f2f3f5;
    --white: #ffffff;
    --backdrop: #e9e1d5;
    --muted: #d9dfea;
  }
  * { box-sizing: border-box; margin: 0; padding: 0; }
  html, body { width: 1200px; height: 687px; overflow: hidden; }
  body {
    background: var(--backdrop);
    font-family: "Jost", "Futura", sans-serif;
    display: flex;
    align-items: center;
    justify-content: center;
    gap: 40px;
  }
  .card {
    width: 540px;
    height: 309px;
    display: flex;
    background: var(--paper);
    box-shadow: 0 14px 30px rgba(60, 45, 25, 0.18);
  }
  .card__brand {
    flex: 0 0 56%;
    display: flex;
    align-items: center;
    justify-content: center;
  }
  .brand-name {
    display: flex;
    align-items: center;
    gap: 10px;
    color: var(--navy);
    font-weight: 700;
    font-size: 22px;
    letter-spacing: 0.02em;
  }
  .brand-name__dot {
    width: 26px;
    height: 26px;
    border-radius: 50%;
    background: var(--red);
    flex: none;
  }
  .card__panel {
    flex: 1;
    background: var(--navy);
    color: var(--white);
    padding: 34px 22px 26px 24px;
    display: flex;
    flex-direction: column;
  }
  .contact__name { font-weight: 700; font-size: 17px; letter-spacing: 0.02em; }
  .contact__title { font-size: 12px; margin-top: 4px; }
  .contact__list { list-style: none; margin-top: auto; font-size: 11px; }
  .contact__row { display: flex; align-items: center; gap: 8px; margin-top: 7px; }
  .contact__row--email { font-size: 9.5px; }
  .contact__icon { width: 18px; height: 18px; flex: none; }
  .contact__locations { font-size: 10px; margin-top: 10px; color: var(--muted); }
  .contact__web { font-weight: 700; font-size: 13px; margin-top: 12px; letter-spacing: 0.02em; }

  .statement { font-size: 12.5px; line-height: 1.45; text-align: center; margin-top: 18px; }
  .statement strong { font-weight: 700; }
  .pledge { margin-top: auto; font-weight: 700; font-size: 11.5px; text-align: center; }
</style>
</head>
<body>

  <section class="card card--front" aria-label="Business card front">
    <div class="card__brand">
      <div class="brand-name"><span class="brand-name__dot"></span>Harborline Energy</div>
    </div>
    <div class="card__panel contact">
      <p class="contact__name">Dale Menschow</p>
      <p class="contact__title">Owner/CEO</p>
      <ul class="contact__list">
        <li class="contact__row">
          <svg class="contact__icon" viewBox="0 0 18 18" aria-hidden="true">
            <circle cx="9" cy="9" r="9" fill="#ffffff"/>
            <path d="M6 4.8c.4-.3.9-.2 1.1.2l.8 1.5c.2.4.1.8-.2 1l-.6.5c.4 1 1.2 1.8 2.1 2.2l.5-.6c.3-.3.7-.4 1-.2l1.5.8c.4.2.5.7.2 1.1l-.6.8c-.4.5-1.1.6-1.7.4C8 11.8 6.2 10 5.3 7.8c-.2-.6-.1-1.3.4-1.7z" fill="#0c2b5c"/>
          </svg>
          555.318.4076
        </li>
        <li class="contact__row contact__row--email">
          <svg class="contact__icon" viewBox="0 0 18 18" aria-hidden="true">
            <circle cx="9" cy="9" r="9" fill="#ffffff"/>
            <rect x="4.5" y="5.8" width="9" height="6.4" rx="0.6" fill="none" stroke="#0c2b5c" stroke-width="1.1"/>
            <path d="M4.8 6.2 9 9.4l4.2-3.2" fill="none" stroke="#0c2b5c" stroke-width="1.1"/>
          </svg>
          DMENSCHOW@HARBORLINEENERGY.EXAMPLE
        </li>
      </ul>
      <p class="contact__locations">Powder River | DJ basin | Bakken formations</p>
      <p class="contact__web">HARBORLINEENERGY.EXAMPLE</p>
    </div>
  </section>

  <section class="card card--back" aria-label="Business card back">
    <div class="card__brand">
      <div class="brand-name"><span class="brand-name__dot"></span>Harborline Energy</div>
    </div>
    <div class="card__panel">
      <p class="statement">
        Frac fueling is <strong>what we do.</strong><br>
        We understand how <strong>important diesel fuel</strong><br>
        is to your operation <strong>which is why our</strong><br>
        main service line <strong>is Frac fueling.</strong>
      </p>
      <p class="pledge">We assure our supply and stand by our service.</p>
    </div>
  </section>

</body>
</html>
```